business card for LWR pty ltd

We require a business card that stands out . I have included our company flyer and would like the services listed to be put on the card so when we Give out the cards to customers they have an idea of services we provide. need the winning design to be in editable photo shop format, editable iMac pages format or editable windows publisher format, so that I can enter in names, email addresses, phone numbers etc myself. I have included a pdf documents of info / items needed on the card to use as reference please.
Updates

need more submissions

Need extra days to review

Sick

Target Market(s)

new customers

Contact Information for Business Card

details are on attached business card requirements file

Requirements
Must have
• I have attached a list of must haves

```html
<!DOCTYPE html>
<html lang="en">
<head>
<meta charset="utf-8">
<title>LWR pty ltd – Business Card</title>
<link href="https://fonts.googleapis.com/css2?family=Quicksand:wght@500;600;700&display=swap" rel="stylesheet">
<style>
  :root{
    --bg:#3a3b3e;
    --card-black:#0b0b0c;
    --steel-dark:#1c1d20;
    --steel-mid:#34363b;
    --band-blue:#10a9ee;
    --accent-blue:#1583de;
    --name-blue:#1a87e0;
    --ink:#1b1b1b;
    --white:#ffffff;
    --earth-light:#c98a55;
    --earth-dark:#8a4a24;
    --sky-night:#101214;
  }
  *{box-sizing:border-box;margin:0;padding:0}
  html,body{width:1200px;height:800px;overflow:hidden}
  body{
    background:var(--bg);
    font-family:"Quicksand",sans-serif;
    display:flex;align-items:center;justify-content:center;gap:40px;
  }
  .card{
    position:relative;width:540px;height:310px;overflow:hidden;
    background:var(--white);
    box-shadow:0 14px 30px rgba(0,0,0,.45);
  }

  /* ---------- Back: fleet side ---------- */
  .card-back .top-strip{position:absolute;left:0;top:0;width:100%;height:10px;background:var(--band-blue)}
  .card-back .hero{position:absolute;left:0;top:10px;width:100%;height:200px;background:var(--card-black)}
  .card-back .hero-steel{
    position:absolute;inset:0;
    background:radial-gradient(ellipse at 62% 45%,var(--steel-mid) 0%,var(--steel-dark) 45%,var(--card-black) 85%);
  }
  .card-back .hero-photo{
    position:absolute;left:0;top:30px;width:58%;height:170px;
    background:linear-gradient(160deg,var(--sky-night) 0%,#2b2a28 35%,var(--earth-dark) 55%,var(--earth-light) 100%);
    clip-path:polygon(0 0,55% 0,100% 100%,0 100%);
  }
  .card-back .brand{
    position:absolute;left:300px;top:70px;transform:translateX(-50%);
    font-size:64px;font-weight:700;letter-spacing:4px;color:#d6d8dc;
  }
  .card-back .band{
    position:absolute;left:0;bottom:0;width:100%;height:100px;background:var(--band-blue);
    display:flex;align-items:center;justify-content:center;
  }
  .card-back .web{color:var(--white);font-size:22px;font-weight:600;letter-spacing:.5px}

  /* ---------- Front: contact side ---------- */
  .card-front .panel{
    position:absolute;left:0;top:0;width:330px;height:100%;background:var(--card-black);
  }
  .card-front .panel-steel{
    position:absolute;inset:0;
    background:radial-gradient(ellipse at 55% 40%,var(--steel-mid) 0%,var(--steel-dark) 45%,var(--card-black) 85%);
  }
  .card-front .edge-accent{position:absolute;left:330px;width:8px;height:52px;background:var(--accent-blue)}
  .card-front .edge-accent.top{top:0}
  .card-front .edge-accent.bottom{bottom:0}
  .card-front .brand{
    position:absolute;left:165px;top:72px;transform:translateX(-50%);
    font-size:64px;font-weight:700;letter-spacing:4px;color:#d6d8dc;
  }
  .card-front .company{
    position:absolute;left:0;width:330px;top:188px;text-align:center;
    color:var(--white);font-size:20px;font-weight:700;
  }
  .card-front .side-tab{position:absolute;right:0;top:110px;width:16px;height:40px;background:var(--accent-blue)}
  .card-front .details{
    position:absolute;right:34px;top:30px;width:180px;text-align:right;color:var(--ink);
  }
  .card-front .name{color:var(--name-blue);font-size:22px;font-weight:600}
  .card-front .role{font-size:15px;font-weight:600;margin-top:2px}
  .card-front .address{font-size:11px;font-weight:600;line-height:1.35;margin-top:26px;padding-right:22px;position:relative}
  .card-front .contact{list-style:none;margin-top:14px}
  .card-front .contact li{
    font-size:11px;font-weight:600;display:flex;justify-content:flex-end;align-items:center;gap:6px;margin-top:7px;white-space:nowrap;
  }
  .card-front .icon{width:15px;height:15px;flex:none}
  .card-front .address .icon{position:absolute;right:0;top:8px}
</style>
</head>
<body>

  <section class="card card-back" aria-label="Business card back">
    <div class="top-strip"></div>
    <div class="hero">
      <div class="hero-steel" role="img" aria-label="Dark perforated steel honeycomb texture"></div>
      <div class="hero-photo" role="img" aria-label="Photograph of a road train truck on red outback dirt"></div>
      <div class="brand">LWR</div>
    </div>
    <div class="band"><span class="web">www.websiteaddress.com</span></div>
  </section>

  <section class="card card-front" aria-label="Business card front">
    <div class="panel">
      <div class="panel-steel" role="img" aria-label="Dark perforated steel honeycomb texture"></div>
      <div class="brand">LWR</div>
      <div class="company">LWR pty ltd</div>
    </div>
    <div class="edge-accent top"></div>
    <div class="edge-accent bottom"></div>
    <div class="side-tab"></div>

    <div class="details">
      <div class="name">Daniel Hart</div>
      <div class="role">Director</div>
      <div class="address">
        Lot 444 example address<br>Australia
        <svg class="icon" viewBox="0 0 16 16" aria-hidden="true"><path d="M8 1a5 5 0 0 0-5 5c0 3.6 5 9 5 9s5-5.4 5-9a5 5 0 0 0-5-5zm0 7a2 2 0 1 1 0-4 2 2 0 0 1 0 4z" fill="var(--accent-blue)"/></svg>
      </div>
      <ul class="contact">
        <li>000 444 000
          <svg class="icon" viewBox="0 0 16 16" aria-hidden="true"><rect width="16" height="16" rx="2" fill="var(--accent-blue)"/><path d="M5 3.5l1.6 2.3-1 1a6 6 0 0 0 2.6 2.6l1-1L11.5 10l-.9 1.6C7 11.5 4.5 9 4.4 5.4z" fill="#fff"/></svg>
        </li>
        <li>www.websiteaddress.com
          <svg class="icon" viewBox="0 0 16 16" aria-hidden="true"><circle cx="8" cy="8" r="7.5" fill="var(--accent-blue)"/><path d="M8 1.5v13M1.5 8h13M8 1.5c-3 3-3 10 0 13M8 1.5c3 3 3 10 0 13" stroke="#fff" stroke-width="1" fill="none"/></svg>
        </li>
        <li>email@lwrservices.com.au
          <svg class="icon" viewBox="0 0 16 16" aria-hidden="true"><rect y="2" width="16" height="12" rx="1.5" fill="var(--accent-blue)"/><path d="M1.5 4l6.5 5 6.5-5" stroke="#fff" stroke-width="1.4" fill="none"/></svg>
        </li>
      </ul>
    </div>
  </section>

</body>
</html>
```